Design an eBook cover for The Honest Chaos Of The Youngest Sibling

The Honest Chaos Of the Youngest Sibling was a blog post written in 2012 that has since gone viral, and read by millions. I am combining it with some other popular posts to make a short eBook designed to appeal to anyone who has three kids, is considering three kids or wants to justify their decision NEVER to have three kids.

Read the post here: http://nappiesandnoise.examplepress.com.au/2012/02/honest-chaos-of-youngest-sibling.html. You can also see the artwork on my blog to get an idea of what I might be looking for.

The book cover must be absolutely eye catching and unambiguous. The book is funny and heart felt, very real and a bit grubby. It can be simple but it must be funny and clever. I would prefer drawings/cartoons rather than photographic images. The cover must allow space for a "quote" from a well-known blogger.

I can't wait to see what you come up with. Thank you!

Target Market(s)

Parents, mothers to be, people with a sense of humour

Font styles to use
Sans Serif

Requirements
Must have
• Eye catching title "The Honest Chaos Of The Youngest Sibling"
• Author name: Bridget Lanvoisey
• Great image
• Space for a 'this is brilliant etc etc' quote from big-name blogger.
• Must be able to be uploaded to Pagewell as an eBook cover
Nice to have
• Pithy one liner explaining the book underneath the main title.
• Memorable picture/image - simple, eye catching.
• Nice to have options for spine and back cover.
• Please look at my blog for more ideas www.nappiesandnoise.examplepress.com
Should not have
• My picture.
• No stock images or photos.

```html
<!DOCTYPE html>
<html lang="en">
<head>
<meta charset="utf-8">
<title>The Honest Chaos Of The Youngest Sibling — eBook Cover</title>
<link rel="stylesheet" href="https://fonts.googleapis.com/css2?family=Archivo+Black&family=Oswald:wght@500;700&family=Source+Sans+3:wght@400&display=swap">
<style>
  :root {
    --page: #ffffff;
    --cover-orange: #f05a24;
    --ink: #333333;
    --paper-light: #e4e4e4;
    --paper-dark: #bcbcbc;
    --muted: #8a8a8a;
    --white: #ffffff;
    --avatar: #6f7fa0;
  }
  html, body {
    margin: 0;
    padding: 0;
    width: 1200px;
    height: 1000px;
    overflow: hidden;
    background: var(--page);
  }
  .canvas {
    position: relative;
    width: 1200px;
    height: 1000px;
  }
  .book-cover {
    position: absolute;
    left: 0;
    top: 0;
  }
  .title-heavy {
    font-family: "Archivo Black", "Arial Black", sans-serif;
    fill: var(--ink);
  }
  .title-sub {
    font-family: "Oswald", "Arial Narrow", sans-serif;
    font-weight: 700;
    fill: var(--ink);
  }
  .author-name {
    font-family: "Oswald", "Arial Narrow", sans-serif;
    font-weight: 500;
    fill: var(--white);
  }
  .quote-meta, .quote-text {
    font-family: "Source Sans 3", "Helvetica Neue", sans-serif;
  }
  .quote-author { fill: var(--muted); }
  .quote-date { fill: var(--cover-orange); }
  .quote-text { fill: #222222; }
</style>
</head>
<body>
<main class="canvas">
  <svg class="book-cover" width="1200" height="1000" viewBox="0 0 1200 1000" xmlns="http://www.w3.org/2000/svg">
    <defs>
      <linearGradient id="stork-tone" x1="0" y1="0" x2="1" y2="1">
        <stop offset="0" stop-color="#fbe0d3"/>
        <stop offset="1" stop-color="#f7b89c"/>
      </linearGradient>
      <linearGradient id="quote-paper" x1="0" y1="0" x2="0" y2="1">
        <stop offset="0" stop-color="var(--paper-dark)"/>
        <stop offset="0.5" stop-color="var(--paper-light)"/>
        <stop offset="1" stop-color="var(--paper-dark)"/>
      </linearGradient>
    </defs>

    <!-- cover board -->
    <rect class="cover-board" x="329" y="76" width="531" height="849" fill="var(--cover-orange)"/>

    <!-- hero illustration area, kept clear of the headline -->
    <rect class="hero-illustration" x="329" y="92" width="472" height="258" rx="6"
          fill="url(#stork-tone)" role="img"
          aria-label="White silhouette of a flying stork carrying a bundle marked with the number 3"/>

    <!-- title -->
    <g class="book-title">
      <text class="title-heavy" x="356" y="440" font-size="108" textLength="202" lengthAdjust="spacingAndGlyphs">THE</text>
      <text class="title-heavy" x="356" y="527" font-size="108" textLength="476" lengthAdjust="spacingAndGlyphs">HONEST</text>
      <text class="title-heavy" x="356" y="612" font-size="108" textLength="370" lengthAdjust="spacingAndGlyphs">CHAOS</text>
      <text class="title-sub" x="356" y="665" font-size="52" textLength="468" lengthAdjust="spacingAndGlyphs">OF THE YOUNGEST SIBLING</text>
    </g>

    <!-- review strip -->
    <g class="review-strip">
      <rect x="415" y="686" width="445" height="112" fill="url(#quote-paper)"/>
      <rect class="review-roll" x="388" y="700" width="42" height="128" rx="6"
            fill="#f2f2f2" stroke="#b5b5b5" transform="rotate(-22 409 764)"/>
      <rect class="review-avatar" x="445" y="729" width="40" height="44"
            fill="var(--avatar)" role="img" aria-label="Reviewer profile picture"/>
      <text class="quote-meta" x="494" y="724" font-size="19">
        <tspan class="quote-author">Anonymous</tspan>
        <tspan class="quote-date">Monday, February 12, 2015</tspan>
      </text>
      <text class="quote-text" x="494" y="752" font-size="19">“A wonderful piece of writing. Heartwarming</text>
      <text class="quote-text" x="494" y="778" font-size="19">and humorous. Thanks for sharing!”</text>
    </g>

    <!-- author -->
    <text class="author-name" x="356" y="902" font-size="62" textLength="476" lengthAdjust="spacingAndGlyphs">BRIDGET LANVOISEY</text>
  </svg>
</main>
</body>
</html>
```